Web Design for an Employment Agency

We need a website design for an employment agency here in New Zealand.

We have attached a few examples of what other designers have submitted but the client is not exactly happy with the concepts and what came out in the end.

They have given this link for some idea of the sketches look they like: http://www.quillbrookgallery.com/artist-fuses-animals-with-nature-pen-sketches/

They have asked to use "maori sketches" in black and white through the website, you can Google "Maori art" or "Maori drawings" to get an idea of the type of drawings that they are.

Please ensure the concept designs incorporate some sort of those maori designs through out the website.

Unfortunately we do not have a lot of copy to work with, but please use filler text and content for areas if need be and we can get extra copy from the client afterwards.

The client does not want people or buildings

Also, the logo should be displayed as it is currently – they do not want to deviate from it.

They also would like Maori type of sketches (in Black and white) the grey colour can be used as a background when you use the logo on the page.

The design must be professional and bold.

The service they offer is all about professionalism.

------------------------------------------------------------------
UPDATE - 20th FEBRUARY

Please see attached file for the brief of the different sections of the website as well as some examples of the maori designs from framelodger.

I have also attached another design she liked the look of the most, but se wanted the following changes made to it:

- She does not want the photo at the top with the hand writing, she wants her logo in a watermark format to show there in the background
- She wants where you have those other images in circle, she wants "maori" type designs to be incorporated somewhere there
- She needs the content that we have provided to be all there on the page in the different sections, I will re-send you the content

Please re-submit your concepts based along the lines of that, please ensure the text and content match the sections and I will send to her for final approval.

Updates

Looking for designs to come through ASAP please

Target Market(s)

New Zealand people looking for jobs, and people looking for workers in NZ

Industry/Entity Type

Employment Agency

Number of Pages Required

4 page

Font styles to use
Sans Serif

Colors

Designer to choose colors to be used in the design.

Requirements
Must have
• It needs to be nice and clean perhaps grey scale like the attached
• The design must be professional and bold.
• They also would like Maori type of sketches (in Black and white) the grey colour can be used as a background when you use the logo on the page.
Nice to have
• You can think about the business, maybe do some of the copy or content as well to make more attractive to the client when I show them
Should not have
• Do not have lots of colour, The client does not want people or buildings

```html
<!DOCTYPE html>
<html lang="en">
<head>
<meta charset="utf-8">
<title>Workvane.net – Employment Agency</title>
<link rel="stylesheet" href="https://fonts.googleapis.com/css2?family=Lato:wght@400;700;900&display=swap">
<style>
  :root {
    --ink: #3a3a3a;
    --dark: #1f1f1f;
    --dark-2: #262626;
    --footer: #202020;
    --band: #e3e3e3;
    --art: #c9ccc9;
    --white: #ffffff;
    --muted: #bdbdbd;
    --rule: #cfcfcf;
  }
  * { box-sizing: border-box; margin: 0; padding: 0; }
  html, body { width: 1200px; height: 3093px; overflow: hidden; }
  body {
    position: relative;
    background: var(--white);
    font-family: "Lato", Arial, sans-serif;
    color: var(--ink);
  }
  .backdrop { position: absolute; inset: 0; width: 1200px; height: 3093px; }
  .abs { position: absolute; }

  /* Header */
  .logo {
    left: 76px; top: 27px; width: 94px; height: 94px; border-radius: 50%;
    background: #e6e6e6; display: flex; align-items: center; justify-content: center;
    font-size: 15px; font-weight: 700; color: #222;
  }
  .nav { right: 74px; top: 64px; display: flex; gap: 40px; }
  .nav a { color: var(--white); text-decoration: none; font-size: 13px; font-weight: 700; letter-spacing: .5px; }

  /* Hero */
  .hero-title { left: 76px; top: 264px; color: var(--white); font-size: 37px; font-weight: 700; letter-spacing: .5px; }
  .hero-lead { left: 76px; top: 326px; color: #e8e8e8; font-size: 18px; }
  .hero-cta { left: 76px; top: 361px; color: var(--white); font-size: 18px; font-weight: 700; }
  .hero-list { left: 76px; top: 396px; list-style: none; }
  .hero-list li { display: flex; align-items: center; gap: 18px; color: #e8e8e8; font-size: 17px; height: 37.5px; }
  .tick { width: 16px; height: 16px; flex: none; }
  .watermark {
    left: 580px; top: 240px; width: 520px; height: 360px;
    display: flex; flex-direction: column; align-items: center; justify-content: flex-end; gap: 30px;
  }
  .watermark-dot { width: 190px; height: 190px; border-radius: 50%; border: 3px solid #333; }
  .watermark-name { font-size: 76px; color: #2c2c2c; font-weight: 400; letter-spacing: 3px; }

  /* Section heads */
  .section-title { font-size: 37px; font-weight: 700; color: var(--ink); }
  .rule { height: 2px; background: var(--rule); }

  /* About */
  .art-circle { border-radius: 50%; background: var(--art); }
  .about-title { left: 526px; top: 806px; }
  .about-rule { left: 526px; top: 861px; width: 268px; }
  .about-copy { left: 526px; top: 884px; width: 610px; font-size: 14.5px; line-height: 28px; color: #444; }
  .about-quote { font-size: 24px; font-weight: 700; color: #333; line-height: 36px; margin-top: 4px; }
  .about-note { left: 0; width: 1200px; top: 1246px; text-align: center; font-size: 14.5px; line-height: 29px; color: #444; }
  .about-note strong { font-weight: 700; }

  /* Services */
  .services-title { left: 0; width: 1200px; top: 1438px; text-align: center; }
  .services-rule { left: 470px; top: 1493px; width: 260px; }
  .services-intro { left: 76px; top: 1572px; font-size: 14.5px; font-weight: 700; color: #333; }
  .services-list { left: 76px; top: 1605px; width: 600px; list-style: none; }
  .services-list li { display: flex; gap: 18px; font-size: 14.5px; line-height: 25px; color: #444; margin-bottom: 12px; }
  .services-list .tick { margin-top: 5px; }
  .services-cta { left: 76px; top: 1855px; width: 560px; font-size: 14.5px; line-height: 25px; font-weight: 700; color: #333; }

  /* Testimonials */
  .testimonials-title { left: 0; width: 1200px; top: 2080px; text-align: center; }
  .testimonials-rule { left: 464px; top: 2138px; width: 272px; }
  .testimonial { top: 2190px; width: 330px; }
  .quote-mark { width: 38px; height: 30px; display: block; margin-bottom: 14px; }
  .testimonial p { font-size: 14.5px; line-height: 28px; color: #444; }
  .testimonial h4 { margin-top: 8px; font-size: 14.5px; font-weight: 700; color: #222; }

  /* Contact */
  .contact-title { left: 0; width: 1200px; top: 2550px; text-align: center; color: var(--white); font-size: 37px; font-weight: 700; }
  .contact-rule { left: 470px; top: 2606px; width: 262px; background: var(--white); }
  .contact-info { left: 0; width: 1200px; top: 2643px; display: flex; justify-content: center; align-items: center; gap: 12px; color: #e6e6e6; font-size: 13.5px; }
  .contact-info svg { width: 13px; height: 13px; vertical-align: -2px; margin-right: 8px; }
  .sep { color: #888; }
  .field {
    background: var(--white); border-radius: 3px; height: 46px;
    font-size: 14px; color: #333; padding: 14px 18px;
  }
  .field-message { height: 89px; }
  .submit {
    left: 497px; top: 2911px; width: 206px; height: 52px; background: #000; color: var(--white);
    display: flex; align-items: center; justify-content: center; font-size: 22px; font-weight: 700; border-radius: 3px;
  }

  /* Footer */
  .footer-line { left: 0; top: 3022px; width: 1200px; height: 1px; background: #3a3a3a; }
  .copyright { left: 76px; top: 3050px; font-size: 12px; color: #d8d8d8; }
  .social { right: 76px; top: 3049px; display: flex; gap: 22px; }
  .social span { width: 17px; height: 17px; border-radius: 50%; background: #e6e6e6; display: block; }
</style>
</head>
<body>

<svg class="backdrop" viewBox="0 0 1200 3093" aria-hidden="true">
  <polygon points="0,0 1200,0 1200,680 0,740" fill="var(--dark)"/>
  <polygon points="0,1412 1200,1351 1200,2037 0,1980" fill="var(--band)"/>
  <polygon points="0,2516 1200,2454 1200,3093 0,3093" fill="var(--dark-2)"/>
  <rect x="0" y="3022" width="1200" height="71" fill="var(--footer)"/>
</svg>

<!-- Header -->
<div class="abs logo">Workvane.net</div>
<nav class="abs nav">
  <a href="#">HOME</a><a href="#">ABOUT</a><a href="#">SERVICE</a><a href="#">TESTIMONIALS</a><a href="#">CONTACT US</a>
</nav>

<!-- Hero -->
<div class="abs watermark" aria-hidden="true">
  <div class="watermark-dot"></div>
  <div class="watermark-name">Workvane.net</div>
</div>
<h1 class="abs hero-title">WHY – WORKVANE.NET?</h1>
<p class="abs hero-lead">Applying for positions and not getting anywhere…….</p>
<p class="abs hero-cta">LET US HELP YOU!</p>
<ul class="abs hero-list">
  <li><svg class="tick" viewBox="0 0 16 16"><circle cx="8" cy="8" r="8" fill="#fff"/><path d="M4.5 8.2l2.3 2.3 4.7-4.7" stroke="#1f1f1f" stroke-width="2" fill="none"/></svg>Face to face meeting – YOU ARE NOT ALONE ANYMORE</li>
  <li><svg class="tick" viewBox="0 0 16 16"><circle cx="8" cy="8" r="8" fill="#fff"/><path d="M4.5 8.2l2.3 2.3 4.7-4.7" stroke="#1f1f1f" stroke-width="2" fill="none"/></svg>Represent yourself professionally</li>
  <li><svg class="tick" viewBox="0 0 16 16"><circle cx="8" cy="8" r="8" fill="#fff"/><path d="M4.5 8.2l2.3 2.3 4.7-4.7" stroke="#1f1f1f" stroke-width="2" fill="none"/></svg>Where to begin searching</li>
  <li><svg class="tick" viewBox="0 0 16 16"><circle cx="8" cy="8" r="8" fill="#fff"/><path d="M4.5 8.2l2.3 2.3 4.7-4.7" stroke="#1f1f1f" stroke-width="2" fill="none"/></svg>Having an agent that acts on your behalf</li>
</ul>

<!-- About -->
<div class="abs art-circle" style="left:76px;top:819px;width:384px;height:384px" role="img" aria-label="Maori style tribal scroll artwork in white on a grey circle"></div>
<h2 class="abs section-title about-title">ABOUT US</h2>
<div class="abs rule about-rule"></div>
<div class="abs about-copy">
  <p>20 years in the Recruitment market – as Candidate, Employer, External &amp; Internal Recruiter - highlighted certain annoying facts about the Recruitment Industry that screamed for a solution!</p>
  <p>After more than 5 years of market research a service addressing the needs of Job Seekers (Candidates) could not be found and we have decided that the question so many candidates ask ….</p>
  <p class="about-quote">“Can you find me a job…..?”</p>
  <p>definitely needed a POSITIVE answer.</p>
</div>
<p class="abs about-note">By offering the service namely, becoming the Job Seekers agent in the employment market, we not only assist our clients (the candidates)<br><strong>BUT we inevitably address the frustrations of the Employers and Recruiters successfully as well..</strong></p>

<!-- Services -->
<h2 class="abs section-title services-title">SERVICES</h2>
<div class="abs rule services-rule"></div>
<p class="abs services-intro">We provide tailormade packages or our standard complete service:</p>
<ul class="abs services-list">
  <li><svg class="tick" viewBox="0 0 16 16"><circle cx="8" cy="8" r="8" fill="#333"/><path d="M4.5 8.2l2.3 2.3 4.7-4.7" stroke="#e3e3e3" stroke-width="2" fill="none"/></svg>Interview / Consultation</li>
  <li><svg class="tick" viewBox="0 0 16 16"><circle cx="8" cy="8" r="8" fill="#333"/><path d="M4.5 8.2l2.3 2.3 4.7-4.7" stroke="#e3e3e3" stroke-width="2" fill="none"/></svg>Professional CV Writing</li>
  <li><svg class="tick" viewBox="0 0 16 16"><circle cx="8" cy="8" r="8" fill="#333"/><path d="M4.5 8.2l2.3 2.3 4.7-4.7" stroke="#e3e3e3" stroke-width="2" fill="none"/></svg><span>Marketing the candidate - Presenting you to Companies seeking your skills and matching the Employers requirements to your field of Expertise (Career Hunting for positions in the market and initial representation at the Employer)</span></li>
  <li><svg class="tick" viewBox="0 0 16 16"><circle cx="8" cy="8" r="8" fill="#333"/><path d="M4.5 8.2l2.3 2.3 4.7-4.7" stroke="#e3e3e3" stroke-width="2" fill="none"/></svg>Self-listing suggestions – positions available</li>
  <li><svg class="tick" viewBox="0 0 16 16"><circle cx="8" cy="8" r="8" fill="#333"/><path d="M4.5 8.2l2.3 2.3 4.7-4.7" stroke="#e3e3e3" stroke-width="2" fill="none"/></svg>2 Written references done</li>
</ul>
<p class="abs services-cta">The first Consultation is free so give us a call or drop us a mail to find the best solution for you..!</p>
<div class="abs art-circle" style="left:742px;top:1551px;width:384px;height:384px" role="img" aria-label="Maori style turtle carving pattern in white on a grey circle"></div>

<!-- Testimonials -->
<h2 class="abs section-title testimonials-title">TESTIMONIALS</h2>
<div class="abs rule testimonials-rule"></div>
<div class="abs testimonial" style="left:76px">
  <svg class="quote-mark" viewBox="0 0 38 30"><path d="M0 30V16C0 7 5 2 14 0v6c-4 1-6 4-6 8h6v16zM22 30V16c0-9 5-14 14-16v6c-4 1-6 4-6 8h6v16z" fill="#333"/></svg>
  <p>Lorem ipsum dolor sit amet, consectetur adipiscing elit. Proin mi dui, vestibulum a orci vel, ultricies consequat felis lobortis enim ligula, nec aliquet elit semper non....”</p>
  <h4>-NAME HEADING</h4>
</div>
<div class="abs testimonial" style="left:435px">
  <svg class="quote-mark" viewBox="0 0 38 30"><path d="M0 30V16C0 7 5 2 14 0v6c-4 1-6 4-6 8h6v16zM22 30V16c0-9 5-14 14-16v6c-4 1-6 4-6 8h6v16z" fill="#333"/></svg>
  <p>Lorem ipsum dolor sit amet, consectetur adipiscing elit. Proin mi dui, vestibulum a orci vel, ultricies consequat felis lobortis enim ligula, nec aliquet elit semper non....”</p>
  <h4>-NAME HEADING</h4>
</div>
<div class="abs testimonial" style="left:794px">
  <svg class="quote-mark" viewBox="0 0 38 30"><path d="M0 30V16C0 7 5 2 14 0v6c-4 1-6 4-6 8h6v16zM22 30V16c0-9 5-14 14-16v6c-4 1-6 4-6 8h6v16z" fill="#333"/></svg>
  <p>Lorem ipsum dolor sit amet, consectetur adipiscing elit. Proin mi dui, vestibulum a orci vel, ultricies consequat felis lobortis enim ligula, nec aliquet elit semper non....”</p>
  <h4>-NAME HEADING</h4>
</div>

<!-- Contact -->
<h2 class="abs contact-title">CONTACT US</h2>
<div class="abs rule contact-rule"></div>
<div class="abs contact-info">
  <span><svg viewBox="0 0 12 16"><path d="M6 0a6 6 0 0 0-6 6c0 4.5 6 10 6 10s6-5.5 6-10a6 6 0 0 0-6-6zm0 8.5A2.5 2.5 0 1 1 6 3.5a2.5 2.5 0 0 1 0 5z" fill="#fff"/></svg>Kauri Bay Auckland</span>
  <span class="sep">|</span>
  <span><svg viewBox="0 0 16 16"><path d="M3.5 0l3 3.5-2 2c1 2.5 3.5 5 6 6l2-2L16 12.5 13.5 16C6 15 1 10 0 2.5z" fill="#fff"/></svg>+64 81 555 0147</span>
  <span class="sep">|</span>
  <span><svg viewBox="0 0 16 12"><path d="M0 0h16v12H0z" fill="#fff"/><path d="M0 0l8 6 8-6" stroke="#262626" stroke-width="1.5" fill="none"/></svg>hello@workvane.net</span>
</div>
<div class="abs field" style="left:254px;top:2689px;width:334px">Name</div>
<div class="abs field" style="left:614px;top:2689px;width:332px">Email Address</div>
<div class="abs field" style="left:254px;top:2747px;width:334px">Phone No</div>
<div class="abs field" style="left:614px;top:2747px;width:332px">Subject</div>
<div class="abs field field-message" style="left:254px;top:2804px;width:692px">Message</div>
<div class="abs submit">Submit</div>

<!-- Footer -->
<div class="abs footer-line"></div>
<p class="abs copyright">Copyright © 2019, Company Name All Right Reserved</p>
<div class="abs social" aria-label="Social links">
  <span></span><span></span><span></span><span></span><span></span><span></span>
</div>

</body>
</html>
```